Dr. Lumora needs a design for its website!

*Only need the design, coding is not required.
*Need desktop version ($500) and mobile/tablet version ($200)
*The attached files are not the exact layout we want, they are just for you to know what information should be included in those pages.
*The function of our website is like www.qtv-medlist.example
*For the background picture, prefer a lively picture and chinese people in it, NOT necessarily need a doctor or sick person in the picture

***Don't just copy the layout from the attachments or from the reference website, we are looking for creative ideas, non-ordinary designs!!!****

We are developing a website for the public to search a doctor by different criteria. At the initial stage, we need 4 pages to start with and other pages at later stage. I have attached the general idea of these pages but not necessarily to be exactly the same, I am looking for some new ideas.

This website needs a professional, modern, simple and user friendly design. The main color to be used in the website will be same as the color (R:0 G:139 B:205) used in our logo (see attached). We don't have any particular thoughts for the other color and the font to be used in the website. Can try to use circle outline for the icon in the navigation bar.

1. Home: will include 4 sections (see attached)

2. Doctor's details (see attached)

3. Health information: will include a short descriptions of this Health Info page and 5 sections (see attached)

4. News (see attached)

Reason: Not too many suitable designs to choose from and need more time to go through the designs

Target Market(s)

All

Industry/Entity Type

Medical

Number of Pages Required

4 page

Requirements
Should not have
• must not be same as or looks too much like www.qtv-medlist.example
• prefer not to use black and red color

```html
<!DOCTYPE html>
<html lang="en">
<head>
<meta charset="utf-8">
<title>Dr. Lumora – Find a Doctor</title>
<link href="https://fonts.googleapis.com/css2?family=Open+Sans:wght@400;600;700;800&display=swap" rel="stylesheet">
<style>
:root{
  --brand:#008bcd;
  --brand-dark:#0a4f74;
  --navy:#0d3d5c;
  --ink:#111;
  --page:#e6e6e6;
  --white:#fff;
  --row-a:#f2f2f2;
  --row-b:#e4e4e4;
  --text:#333;
  --footer:#1d1d1d;
  --field-dark:#333;
  --pink:#e2476f;
}
*{box-sizing:border-box;margin:0;padding:0}
html,body{width:805px;height:1200px;overflow:hidden}
body{background:var(--page);font-family:"Open Sans",Arial,sans-serif;color:var(--text);position:relative}
.site{position:absolute;left:10px;top:10px;width:785px;height:1180px;background:var(--white);overflow:hidden}
.abs{position:absolute}

/* header */
.brand{left:20px;top:10px;display:flex;align-items:center;gap:8px}
.brand-mark{width:48px;height:48px;border-radius:50%;background:var(--brand)}
.brand-name{font-size:30px;font-weight:400;color:var(--brand);letter-spacing:-.5px}
.login-tab{left:400px;top:0;width:385px;height:33px}
.login-form{left:440px;top:8px;display:flex;gap:6px}
.login-form span{display:block;width:101px;height:16px;background:#eee;border-radius:2px;font-size:8px;font-weight:600;color:#333;padding:2px 6px}
.login-form .btn{width:88px;background:var(--brand-dark);color:#fff;text-align:center;font-weight:700;border:1px solid #5fb2dd}
.langs{right:28px;top:50px;font-size:9px;color:#555}
.langs b{color:var(--brand);font-weight:700}

.nav{left:0;top:87px;width:785px;height:33px;background:var(--brand)}
.nav ul{list-style:none;display:flex;height:100%;padding-left:60px}
.nav li{color:#fff;font-size:10.5px;font-weight:700;line-height:33px;padding:0 20px}
.nav li.active{background:var(--navy)}
.nav-search{left:537px;top:7px;width:168px;height:18px;background:#fff;border-radius:9px;font-size:9px;font-weight:700;color:#222;padding:2px 8px;display:flex;align-items:center;gap:4px}

/* hero */
.hero-photo{left:0;top:120px;width:785px;height:400px;background:linear-gradient(180deg,#c9d3db 0%,#e9edf1 35%,#d9e5ef 70%,#bcd2e6 100%)}
.finder{left:42px;top:242px;width:718px;height:213px;background:rgba(40,40,40,.55);border:1px solid rgba(255,255,255,.6);border-radius:3px}
.finder-title{left:58px;top:20px;font-size:19px;font-weight:700;color:#fff}
.finder-title span{color:var(--brand)}
.finder-lens{left:-20px;top:-20px}
.view-all{left:567px;top:18px;width:170px;height:24px;background:var(--brand);border-radius:2px;color:#fff;font-size:8.5px;font-weight:700;display:flex;align-items:center;justify-content:center;gap:8px}
.finder-form{left:11px;top:54px;width:696px;height:148px;background:rgba(0,139,205,.82);border:1px solid rgba(255,255,255,.7);border-radius:3px}
.field{position:absolute}
.field label{display:block;font-size:9px;font-weight:700;color:#fff;margin-bottom:3px}
.field .box{width:241px;height:26px;background:#fff;border-radius:2px;font-size:8.5px;font-weight:600;color:#222;padding:7px 9px;position:relative}
.field .box.sel::after{content:"";position:absolute;right:10px;top:11px;border:5px solid transparent;border-top:5px solid #444}
.btn-search{left:7px;top:112px;width:174px;height:26px;background:var(--navy);color:#fff;font-size:10px;font-weight:700;display:flex;align-items:center;justify-content:center;gap:6px;border-radius:2px}
.btn-reset{left:191px;top:112px;width:174px;height:26px;background:var(--ink);color:#fff;font-size:10px;font-weight:700;display:flex;align-items:center;justify-content:center;border-radius:2px}

/* features */
.band{left:0;top:490px;width:785px;height:165px}
.feature{position:absolute;width:140px;text-align:center;color:#fff;font-size:10.5px;font-weight:700;line-height:1.4}
.feature .ring{width:86px;height:86px;margin:0 auto 8px;border-radius:50%;background:#fff;border:3px solid #fff;box-shadow:0 0 0 2px var(--brand),0 0 0 3px #fff;display:flex;align-items:center;justify-content:center}
.band-shadow{left:30px;top:652px;width:725px;height:14px;background:radial-gradient(ellipse at top,rgba(0,0,0,.3),rgba(0,0,0,0) 70%)}

/* results */
.results-title{left:0;width:785px;top:683px;text-align:center;font-size:15.5px;font-weight:700;color:#222;display:flex;justify-content:center;align-items:center;gap:6px}
.results{left:31px;top:728px;width:723px;border-collapse:collapse;font-size:10px}
.results th{background:var(--navy);color:#fff;font-weight:700;height:39px;border-right:1px solid #fff}
.results th:first-child{border-top-left-radius:5px}
.results th:last-child{border-top-right-radius:5px;border-right:0}
.results td{height:33px;color:#333;border-right:1px solid #fff;padding:0 14px}
.results td:last-child{border-right:0;padding:0 8px}
.results tr:nth-child(odd) td{background:var(--row-a)}
.results tr:nth-child(even) td{background:var(--row-b)}
.c{text-align:center}

/* footer */
.footer{left:0;top:962px;width:785px;height:194px;background:var(--footer)}
.foot-brand{left:40px;top:72px;display:flex;align-items:center;gap:8px}
.foot-brand .brand-mark{background:#ddd;width:44px;height:44px}
.foot-brand .brand-name{color:#ddd;font-size:27px}
.foot-about{left:282px;top:28px;width:182px}
.foot-h{font-size:11px;font-weight:700;color:#fff;margin-bottom:7px}
.foot-about p{font-size:7.6px;line-height:1.5;color:#999}
.foot-contact{left:542px;top:28px;width:205px}
.foot-contact .in{background:#3a3a3a;height:20px;margin-bottom:4px;font-size:7px;color:#aaa;padding:5px 9px;border-radius:1px}
.foot-contact .in.msg{height:45px}
.foot-contact .submit{width:70px;height:19px;background:var(--field-dark);color:#fff;font-size:9px;font-weight:700;text-align:center;line-height:19px;margin-top:4px}
.bottom-bar{left:0;top:1156px;width:785px;height:24px;background:var(--brand);color:#fff;font-size:7px;font-weight:700;padding:0 22px;display:flex;align-items:center;justify-content:space-between}
.socials{display:flex;gap:3px}
.socials i{display:block;width:14px;height:14px;border-radius:50%;background:#fff}
</style>
</head>
<body>
<div class="site">

  <!-- header -->
  <div class="abs brand"><span class="brand-mark"></span><span class="brand-name">Dr. Lumora</span></div>
  <svg class="abs login-tab" viewBox="0 0 385 33" aria-hidden="true"><path d="M0 0H385L365 33H20Z" fill="#008bcd"/></svg>
  <div class="abs login-form"><span>Login Email</span><span>Password</span><span class="btn">LOGIN</span></div>
  <div class="abs langs"><b>ENGLISH</b> &nbsp;|&nbsp; 普通话 &nbsp;|&nbsp; 中文</div>

  <nav class="abs nav">
    <ul><li class="active">HOME</li><li>HEALTH INFO</li><li>NEWS</li><li>ABOUT US</li><li>CONTACT US</li></ul>
    <div class="abs nav-search">
      <svg width="9" height="9" viewBox="0 0 10 10"><circle cx="4" cy="4" r="3" fill="none" stroke="#222" stroke-width="1.4"/><path d="M6.3 6.3L9 9" stroke="#222" stroke-width="1.4"/></svg>SEARCH</div>
  </nav>

  <!-- hero -->
  <div class="abs hero-photo" role="img" aria-label="Photo of a smiling group of young doctors in white coats"></div>

  <div class="abs finder">
    <svg class="abs finder-lens" width="52" height="52" viewBox="0 0 52 52" aria-hidden="true">
      <circle cx="22" cy="22" r="17" fill="#fff" stroke="#111" stroke-width="5"/>
      <circle cx="22" cy="22" r="10" fill="#111"/>
      <path d="M34 34L48 48" stroke="#111" stroke-width="7" stroke-linecap="round"/>
    </svg>
    <div class="abs finder-title">FIND A <span>DOCTOR</span></div>
    <div class="abs view-all">
      <svg width="24" height="14" viewBox="0 0 24 14"><g fill="#fff"><rect x="0" y="0" width="3" height="3"/><rect x="0" y="5.5" width="3" height="3"/><rect x="0" y="11" width="3" height="3"/><rect x="5" y="0" width="19" height="3"/><rect x="5" y="5.5" width="19" height="3"/><rect x="5" y="11" width="19" height="3"/></g></svg>
      VIEW ALL LISTINGS</div>
    <div class="abs finder-form">
      <div class="field" style="left:7px;top:9px"><label>DOCTOR'S NAME</label><div class="box"></div></div>
      <div class="field" style="left:262px;top:9px"><label>SPECIALISM</label><div class="box sel">PLEASE SELECT</div></div>
      <div class="field" style="left:517px;top:9px"><label>DISTRICT</label><div class="box sel" style="width:174px">PLEASE SELECT</div></div>
      <div class="field" style="left:7px;top:63px"><label>GENDER</label><div class="box sel">PLEASE SELECT</div></div>
      <div class="field" style="left:262px;top:63px"><label>SYMPTOMS</label><div class="box sel">PLEASE SELECT</div></div>
      <div class="field" style="left:517px;top:63px"><label>PHONE NUMBER</label><div class="box" style="width:174px"></div></div>
      <div class="abs btn-search"><svg width="15" height="15" viewBox="0 0 16 16"><circle cx="9" cy="7" r="5" fill="none" stroke="#fff" stroke-width="2"/><path d="M5.5 10.5L1.5 14.5" stroke="#fff" stroke-width="2.4"/></svg>SEARCH</div>
      <div class="abs btn-reset">RESET</div>
    </div>
  </div>

  <!-- features band -->
  <svg class="abs band" viewBox="0 0 785 165" preserveAspectRatio="none" aria-hidden="true">
    <path d="M0 25Q392 75 785 25V165H0Z" fill="#008bcd"/>
  </svg>
  <div class="abs band-shadow"></div>

  <div class="feature" style="left:51px;top:485px">
    <div class="ring"><svg width="46" height="40" viewBox="0 0 46 40" fill="none" stroke="#008bcd" stroke-width="2"><rect x="8" y="3" width="34" height="30" rx="2"/><path d="M8 10H3V33a3 3 0 0 0 6 0"/><path d="M14 10h22M14 16h10M14 22h10M14 28h10M30 16v12M24 22h12"/></svg></div>
    First-Hand Health News</div>
  <div class="feature" style="left:189px;top:497px">
    <div class="ring"><svg width="40" height="46" viewBox="0 0 40 46" fill="none" stroke="#008bcd" stroke-width="2"><circle cx="20" cy="17" r="14"/><circle cx="20" cy="17" r="9"/><path d="M20 11l2 4 4 .5-3 3 .8 4-3.8-2-3.8 2 .8-4-3-3 4-.5z"/><path d="M11 28L6 42l6-2 3 5 4-12M29 28l5 14-6-2-3 5-4-12"/></svg></div>
    Exclusive Promotions</div>
  <div class="feature" style="left:333px;top:507px">
    <div class="ring"><svg width="44" height="44" viewBox="0 0 44 44" fill="none" stroke="#008bcd" stroke-width="2"><rect x="12" y="6" width="26" height="34" rx="2"/><rect x="19" y="2" width="12" height="7" rx="1"/><path d="M24 20h10M24 26h10M24 32h10"/><path d="M4 18l9-3 9 3v8c0 6-4 9-9 11-5-2-9-5-9-11z" fill="#fff"/><path d="M9 25l3 3 6-6"/></svg></div>
    Instant Health Advices</div>
  <div class="feature" style="left:473px;top:497px">
    <div class="ring"><svg width="44" height="44" viewBox="0 0 44 44" fill="none" stroke="#008bcd" stroke-width="2"><rect x="6" y="4" width="32" height="22" rx="1"/><path d="M22 26v4"/><circle cx="30" cy="11" r="2.5" fill="#008bcd"/><path d="M27 22v-6h6v6M30 16l-6-4"/><circle cx="11" cy="33" r="3" fill="#008bcd"/><circle cx="22" cy="33" r="3" fill="#008bcd"/><circle cx="33" cy="33" r="3" fill="#008bcd"/><path d="M6 42a5 5 0 0 1 10 0M17 42a5 5 0 0 1 10 0M28 42a5 5 0 0 1 10 0"/></svg></div>
    Free Health Seminars</div>
  <div class="feature" style="left:614px;top:485px">
    <div class="ring"><svg width="40" height="46" viewBox="0 0 40 46" fill="#008bcd"><circle cx="20" cy="13" r="9"/><path d="M4 44c0-11 7-17 16-17s16 6 16 17z"/><path d="M14 30v6a4 4 0 0 0 8 0" stroke="#fff" stroke-width="1.6" fill="none"/><circle cx="27" cy="36" r="2.5" fill="#fff"/></svg></div>
    Priority Doctor Appointments</div>

  <!-- results -->
  <div class="abs results-title">
    <svg width="24" height="20" viewBox="0 0 24 20"><circle cx="9" cy="5" r="4" fill="#008bcd"/><path d="M1 19c0-6 4-9 8-9s8 3 8 9z" fill="#008bcd"/><circle cx="18" cy="14" r="3.2" fill="#fff" stroke="#0d3d5c" stroke-width="1.6"/><path d="M20.3 16.3L23 19" stroke="#0d3d5c" stroke-width="1.8"/></svg>
    SEARCH RESULTS</div>

  <table class="abs results">
    <colgroup><col style="width:190px"><col style="width:64px"><col style="width:121px"><col style="width:80px"><col style="width:107px"><col style="width:78px"><col style="width:83px"></colgroup>
    <thead><tr><th>Name</th><th>Gender</th><th>Specialism</th><th>Hospital</th><th>Address</th><th>District</th><th>Phone</th></tr></thead>
    <tbody>
      <tr><td>Lau Marcus</td><td class="c"><svg width="14" height="16" viewBox="0 0 14 16"><circle cx="7" cy="4" r="3.5" fill="#0d3d5c"/><path d="M0 16c0-5 3-7.5 7-7.5s7 2.5 7 7.5z" fill="#0d3d5c"/></svg></td><td>Cardiology</td><td class="c">Private</td><td>18 Harbour View Rd</td><td>Kwai Tsing</td><td>123-456-7890</td></tr>
      <tr><td>Tsang Wai Yan, Grace</td><td class="c"><svg width="14" height="16" viewBox="0 0 14 16"><circle cx="7" cy="4" r="3.5" fill="#e2476f"/><path d="M0 16c0-5 3-7.5 7-7.5s7 2.5 7 7.5z" fill="#e2476f"/></svg></td><td>Dentistry</td><td class="c">Private</td><td>7 Orchard Ln</td><td>Kowloon</td><td>234-567-8901</td></tr>
      <tr><td>Yip K W Daniel</td><td class="c"><svg width="14" height="16" viewBox="0 0 14 16"><circle cx="7" cy="4" r="3.5" fill="#0d3d5c"/><path d="M0 16c0-5 3-7.5 7-7.5s7 2.5 7 7.5z" fill="#0d3d5c"/></svg></td><td>Endocrinology</td><td class="c">Private</td><td>96 Maple Terrace</td><td>Sai Kung</td><td>345-678-9012</td></tr>
      <tr><td>Fung Tak, Oliver</td><td class="c"><svg width="14" height="16" viewBox="0 0 14 16"><circle cx="7" cy="4" r="3.5" fill="#0d3d5c"/><path d="M0 16c0-5 3-7.5 7-7.5s7 2.5 7 7.5z" fill="#0d3d5c"/></svg></td><td>Gastroenterology</td><td class="c">Private</td><td>31 Cedar Hill Rd</td><td>Tai Po</td><td>456-789-0123</td></tr>
      <tr><td>Ho Mei Lin</td><td class="c"><svg width="14" height="16" viewBox="0 0 14 16"><circle cx="7" cy="4" r="3.5" fill="#e2476f"/><path d="M0 16c0-5 3-7.5 7-7.5s7 2.5 7 7.5z" fill="#e2476f"/></svg></td><td>General Surgery</td><td class="c">Private</td><td>54 Lantern St</td><td>Wan Chai</td><td>567-890-1234</td></tr>
    </tbody>
  </table>

  <!-- footer -->
  <footer class="abs footer">
    <div class="abs foot-brand"><span class="brand-mark"></span><span class="brand-name">Dr. Lumora</span></div>
    <div class="abs foot-about">
      <h3 class="foot-h">ABOUT DR LUMORA</h3>
      <p>Lorem ipsum dolor sit amet, consectetuer adipiscing elit, sed diam nonummy nibh euismod tincidunt ut laoreet dolore magna aliquam erat volutpat. Ut wisi enim ad min im veniam, quis nostrud exerci tation ullam corper suscipit lobortis nisl ut aliquip ex ea commodo consequat. Duis autem vel eum iriure dolor in hendrerit in vulputate velit esse molestie consequat, vel illum.</p>
    </div>
    <div class="abs foot-contact">
      <h3 class="foot-h">CONTACT US</h3>
      <div class="in">Name</div>
      <div class="in">Email</div>
      <div class="in msg">Message</div>
      <div class="submit">SUBMIT</div>
    </div>
  </footer>
  <div class="abs bottom-bar"><span>COPYRIGHT © 2016 DR LUMORA. ALL RIGHTS RESERVED.</span><span class="socials"><i></i><i></i><i></i></span></div>
</div>
</body>
</html>
```